Skyward Rovers

I would like to re-fresh my existing web page with something more elegant and professional and what will match with my new logo. From the page it should be clearly seen that I organize and sell flying safaris, it should not be tightened only to Africa, should be general.

Page to be re-freshed:
http://skyward-rovers.example

Target Market(s)

Pilots and non-pilots who are going to have a bush flying safari in Africa

Industry/Entity Type

It Professional

```html
<!DOCTYPE html>
<html lang="en">
<head>
<meta charset="utf-8">
<title>Skyward Rovers – Flying Safaris</title>
<link href="https://fonts.googleapis.com/css2?family=Open+Sans:wght@300;400;600;700&family=Alegreya+Sans:wght@500;700&display=swap" rel="stylesheet">
<style>
:root{
  --page:#ffffff;
  --header-bg:#f1f1f4;
  --ink:#222222;
  --muted:#666666;
  --green:#7c9a1e;
  --brown:#6b4a25;
  --red:#a5201c;
  --orange:#f07d10;
  --box-green:#80a026;
  --box-brown:#97704a;
  --box-red:#c13a31;
  --box-orange:#ee7a22;
  --yellow:#f7a91a;
  --footer:#4a4a4d;
  --footer-text:#a8a8a8;
  --footer-green:#a6c632;
}
*{margin:0;padding:0;box-sizing:border-box}
html,body{width:1139px;height:1200px;overflow:hidden;background:var(--page)}
body{font-family:"Open Sans",sans-serif;color:var(--ink)}
.page{position:relative;width:1139px;height:1200px;overflow:hidden}
.abs{position:absolute}

.site-header{left:0;top:0;width:1139px;height:101px;background:var(--header-bg)}
.brand{left:158px;top:30px;display:flex;align-items:center;gap:10px}
.brand-mark{width:24px;height:24px;border-radius:50%;background:var(--ink)}
.brand-name{font-family:"Alegreya Sans",sans-serif;font-weight:500;font-size:28px;color:var(--ink);letter-spacing:.5px}
.top-links{right:158px;top:20px;font-size:11px;color:#555}
.top-links span.sep{margin:0 9px;color:#777}
.main-nav{right:158px;top:54px;display:flex;gap:34px;font-family:"Alegreya Sans",sans-serif;font-weight:700;font-size:15px}
.main-nav .n1{color:var(--green)}.main-nav .n2{color:var(--brown)}.main-nav .n3{color:var(--red)}.main-nav .n4{color:var(--orange);margin-left:10px}

.hero{left:0;top:101px;width:1139px;height:540px;
  background:
   radial-gradient(ellipse 330px 260px at 470px 240px,rgba(226,148,42,.95),rgba(190,100,20,.6) 55%,transparent 80%),
   radial-gradient(ellipse 300px 300px at 1000px 150px,rgba(150,140,60,.7),transparent 70%),
   linear-gradient(90deg,#2b1d0c,#5a3c14 40%,#4a3a18 75%,#3b3012);}
.hero-fade{left:0;top:480px;width:1139px;height:170px;background:linear-gradient(rgba(255,255,255,0),#fff 85%)}
.hero-caption{right:158px;top:501px;font-size:12px;color:#fff}

.tour-box{top:541px;width:193px;height:175px;color:#fff;text-align:center;padding:0 9px}
.tour-box h2{font-family:"Alegreya Sans",sans-serif;font-weight:700;font-size:20px;margin-top:43px;text-shadow:0 1px 2px rgba(0,0,0,.3)}
.tour-box p{font-size:12.6px;line-height:16px;margin-top:12px}
.box-guided{left:158px;background:var(--box-green)}
.box-self{left:368px;background:var(--box-brown)}
.box-sample{left:579px;background:var(--box-red)}
.box-build{left:789px;background:var(--box-orange)}

.welcome{left:158px;top:736px;font-weight:300;font-size:24.5px;color:var(--orange);white-space:nowrap}
.rule{left:158px;top:775px;width:823px;height:1px;background:linear-gradient(90deg,transparent,#ddd 15%,#ddd 85%,transparent)}
.lead{left:158px;top:792px;width:545px;font-size:15.6px;line-height:21px;color:#333}
.body-copy{left:158px;top:869px;width:565px;font-size:11px;line-height:23.6px;color:#555}

.training{left:750px;top:796px;width:230px;height:116px;background:var(--yellow);padding:8px 15px}
.training h3{font-family:"Alegreya Sans",sans-serif;font-weight:700;font-size:21px;color:#fff}
.training .kicker{font-size:9.5px;line-height:12px;color:#3a2a00;text-transform:uppercase;margin-top:3px}
.training .more{position:absolute;right:16px;top:70px;font-size:10px;color:var(--red);text-decoration:underline}
.plane-art{left:746px;top:888px;width:176px;height:46px;background:linear-gradient(90deg,#222,#111);opacity:.9;border-radius:23px 6px 23px 6px}
.training-note{left:750px;top:940px;width:230px;font-size:11px;line-height:13px;color:#111}

.site-footer{left:0;top:1054px;width:1139px;height:146px;background:var(--footer)}
.giraffe-art{left:35px;top:1042px;width:114px;height:158px;background:linear-gradient(#c59a55,#9a7138);opacity:.85;border-radius:40px 40px 0 0}
.footer-brand{left:159px;top:1091px;display:flex;align-items:center;gap:8px}
.footer-brand .brand-mark{background:#fff;width:18px;height:18px}
.footer-brand .brand-name{color:#fff;font-size:20px}
.copyright{left:173px;top:1132px;font-size:11px;color:var(--footer-text)}
.contact{left:326px;top:1089px;font-size:11px;line-height:13px;color:var(--footer-text)}
.contact .email{color:#fff;font-size:11.5px;margin-top:12px}
.foot-links{top:1089px;font-size:11px;line-height:18.4px;list-style:none}
.foot-tours{left:537px;color:var(--footer-green)}
.foot-site{left:656px;color:var(--orange)}
.languages{left:752px;top:1089px;color:#fff}
.languages h4{font-size:11px;font-weight:600;margin-left:4px}
.lang-row{display:flex;gap:14px;margin-top:10px}
.lang{width:32px;text-align:center;font-size:10.5px;color:#ddd}
.lang svg{display:block;margin:0 auto 6px}
.plane-photo{left:937px;top:1112px;width:202px;height:88px;background:linear-gradient(135deg,#5a6470,#9aa6b0 55%,#c9542c 80%,#6b7580);opacity:.85;border-radius:60px 0 0 0}
</style>
</head>
<body>
<div class="page">

<header class="site-header abs">
  <div class="brand abs"><span class="brand-mark"></span><span class="brand-name">Skyward Rovers</span></div>
  <nav class="top-links abs">Home<span class="sep">|</span>Training<span class="sep">|</span>PPL Validation<span class="sep">|</span>Gallery</nav>
  <nav class="main-nav abs"><span class="n1">Guided Tours</span><span class="n2">Self Guided Tours</span><span class="n3">Sample Tours</span><span class="n4">Build Your Trip</span></nav>
</header>

<div class="hero abs" role="img" aria-label="Photograph of a roaring lion with a golden mane against a blurred green savanna"></div>
<div class="hero-fade abs"></div>
<div class="hero-caption abs">South Africa,&nbsp; Savanna Reserve</div>

<section class="tour-box box-guided abs"><h2>Guided Tours</h2><p>For the social pilot who wants to enjoy a luxury safari flying in the bush</p></section>
<section class="tour-box box-self abs"><h2>Self Guided Tours</h2><p>For the more adventurous &amp; experienced pilot, wanting to set off on his/her own</p></section>
<section class="tour-box box-sample abs"><h2>Sample Tours</h2><p>Check our sample tours to give your the feeling of the options</p></section>
<section class="tour-box box-build abs"><h2>Build Your Trip</h2><p>Try to design your own tour so we can review &amp; send an offer accordingly</p></section>

<h1 class="welcome abs">Welcome to the world of skyward rovers for the adventure of a lifetime</h1>
<div class="rule abs"></div>

<p class="lead abs">All the most pristine and unspoiled places are without doubt off the beaten track, often only accessible by air. If it's a genuine rustic and wild experience you're after, the adventures are only waiting.</p>
<p class="body-copy abs">But you will not find these in any guidebook or airport listing. For a pilot, as for anyone else, these adventures come at a price; usually in the form of accessibility problems and the lack of those creature comforts we've gotten so used to (air traffic control, windsocks, tarmac, avgas, aircraft mechanics etc.), not to mention unpredictable weather and far distances from help. Bush flying has entered the world of aviation and popular culture as a rugged, romantic lifestyle that combines elements of great beauty and independence with a certain degree of risk and danger.</p>

<aside class="training abs">
  <h3>The Bush Pilot Training</h3>
  <p class="kicker">A valuable addition to your flying safari - the bushpilot training course</p>
  <span class="more">know more</span>
</aside>
<div class="plane-art abs" role="img" aria-label="Silhouette of a high-wing bush plane"></div>
<p class="training-note abs">Learn the techniques to be a confident and safe Bush Pilot in Africa. A certificate is issued after completion of the course.</p>

<footer class="site-footer abs"></footer>
<div class="giraffe-art abs" role="img" aria-label="Illustration of a standing giraffe"></div>
<div class="footer-brand abs"><span class="brand-mark"></span><span class="brand-name">Skyward Rovers</span></div>
<div class="copyright abs">Copyright © 2012-2013</div>
<div class="contact abs">
  <div>Tomas Brenner</div><div>+41 70 555 01 23</div><div>Lakeside, Switzerland</div>
  <div class="email">info@skyward-rovers.example</div>
</div>
<ul class="foot-links foot-tours abs"><li>Guide Tours</li><li>Self Guided Tours</li><li>Sample Tours</li><li>Build Your Trip</li></ul>
<ul class="foot-links foot-site abs"><li>Home</li><li>About Us</li><li>Gallery</li><li>Contact Us</li></ul>
<div class="languages abs">
  <h4>WE SPEAK</h4>
  <div class="lang-row">
    <div class="lang"><svg width="22" height="22" viewBox="0 0 22 22"><clipPath id="c1"><circle cx="11" cy="11" r="11"/></clipPath><g clip-path="url(#c1)"><rect width="22" height="22" fill="#1f3f8f"/><path d="M0 0L22 22M22 0L0 22" stroke="#fff" stroke-width="4"/><path d="M0 0L22 22M22 0L0 22" stroke="#c8102e" stroke-width="1.5"/><path d="M11 0V22M0 11H22" stroke="#fff" stroke-width="6"/><path d="M11 0V22M0 11H22" stroke="#c8102e" stroke-width="3.5"/></g></svg>English</div>
    <div class="lang"><svg width="22" height="22" viewBox="0 0 22 22"><clipPath id="c2"><circle cx="11" cy="11" r="11"/></clipPath><g clip-path="url(#c2)"><rect width="22" height="8" fill="#111"/><rect y="7.3" width="22" height="7.4" fill="#dd0000"/><rect y="14.7" width="22" height="7.3" fill="#ffce00"/></g></svg>German</div>
    <div class="lang"><svg width="22" height="22" viewBox="0 0 22 22"><clipPath id="c3"><circle cx="11" cy="11" r="11"/></clipPath><g clip-path="url(#c3)"><rect width="22" height="11" fill="#fff"/><rect y="11" width="22" height="11" fill="#dc143c"/></g></svg>Polish</div>
  </div>
</div>
<div class="plane-photo abs" role="img" aria-label="Photograph of a red and white bush plane flying over mountains"></div>

</div>
</body>
</html>
```